Instagram ad design required

For an IT system house, we need an ad design for a job recruiting campaign on Instagram. A great engaging advertisement is required that encourages potential applicants to click on the ad. The recruiting funnel already exists, only an Instagram ad image should be designed. Follow-up orders for further campaigns as well as Facebook and LinkedIn are possible.
The design of the IT system house Dolvira serves as a design inspiration: www.dolvira.com
The customer should be perceived as a great, modern employer. The target group are young IT technicians who want to work in a cool and modern company. For example, the topic could be IT Super Hero wanted with corresponding graphic content.
Target Market(s)
IT system technician
Industry/Entity Type
Informatik
Other font styles liked:
- PT Sans
Look and feel

```html
<!DOCTYPE html>
<html lang="en">
<head>
<meta charset="utf-8">
<title>Dolvira – We Are Hiring</title>
<link rel="stylesheet" href="https://fonts.googleapis.com/css2?family=Montserrat:wght@500;600;700;800&display=swap">
<style>
  :root {
    --frame: #111111;
    --paper: #f0f0f0;
    --white: #ffffff;
    --green: #27905e;
    --green-deep: #1f7a4f;
    --ink: #2b2b2b;
    --dark: #252525;
  }
  * { margin: 0; padding: 0; box-sizing: border-box; }
  html, body { width: 1200px; height: 1200px; overflow: hidden; background: var(--frame); }
  .ad {
    position: relative;
    width: 1200px; height: 1200px;
    background: var(--frame);
    font-family: "Montserrat", sans-serif;
    color: var(--white);
  }
  .ad-shapes { position: absolute; inset: 0; }
  .brand {
    position: absolute; left: 92px; top: 150px;
    display: flex; align-items: center; gap: 14px;
  }
  .brand-square { width: 44px; height: 44px; background: var(--green); }
  .brand-name { font-size: 46px; font-weight: 800; color: var(--green); letter-spacing: 0.5px; }
  .contact {
    position: absolute; right: 92px; top: 122px; text-align: right; line-height: 1;
  }
  .contact-label { font-size: 26px; font-weight: 500; display: block; }
  .contact-phone { font-size: 38px; font-weight: 600; display: block; margin-top: 8px; }
  .headline { position: absolute; left: 92px; top: 404px; line-height: 1; }
  .headline-intro { display: block; font-size: 44px; font-weight: 500; }
  .headline-main { display: block; font-size: 88px; font-weight: 800; margin-top: 14px; letter-spacing: -1px; }
  .headline-sub { display: block; font-size: 88px; font-weight: 800; line-height: 0.96; margin-top: 2px; letter-spacing: -1px; }
  .tagline {
    position: absolute; left: 92px; top: 764px; width: 360px;
    font-size: 26px; font-weight: 500; line-height: 1.22;
  }
  .cta {
    position: absolute; left: 92px; top: 1021px; width: 211px; height: 47px;
    border-radius: 24px; background: var(--dark); overflow: hidden;
  }
  .cta-label {
    position: absolute; left: 0; top: 0; width: 169px; height: 47px; border-radius: 24px;
    background: var(--green); font-size: 27px; font-weight: 700;
    display: flex; align-items: center; justify-content: center;
  }
  .cta-arrow { position: absolute; right: 14px; top: 12px; }
  .website {
    position: absolute; left: 92px; top: 1082px;
    font-size: 33px; font-weight: 500; color: var(--ink);
  }
</style>
</head>
<body>
<div class="ad">
  <svg class="ad-shapes" width="1200" height="1200" viewBox="0 0 1200 1200">
    <defs>
      <linearGradient id="photoTones" x1="0" y1="0" x2="1" y2="1">
        <stop offset="0" stop-color="#c9a07a"/>
        <stop offset="0.35" stop-color="#6f8a4a"/>
        <stop offset="0.6" stop-color="#d68a2a"/>
        <stop offset="0.85" stop-color="#5d7fa6"/>
        <stop offset="1" stop-color="#8a8a84"/>
      </linearGradient>
    </defs>
    <rect class="canvas-paper" x="24" y="24" width="1152" height="1152" fill="var(--paper)"/>
    <polygon class="light-wedge" points="545,24 1176,24 1176,290 650,290" fill="var(--white)"/>
    <polygon class="light-wedge" points="913,968 1176,968 1176,1176 994,1176" fill="var(--white)"/>
    <path class="contact-band" d="M690,93 H1176 V227 H745 Q730,227 724,213 L680,108 Q676,93 690,93 Z" fill="var(--green)"/>
    <path class="photo-area" role="img" aria-label="Photo: young professional working on a laptop, seated outdoors among green plants"
      d="M303,255 H1120 Q1176,255 1176,311 V969 H620 Q570,969 550,925 L303,255 Z" fill="url(#photoTones)"/>
    <path class="headline-panel" d="M24,294 H430 Q478,294 495,340 L700,905 Q712,952 665,952 H24 Z" fill="var(--green)" opacity="0.94"/>
    <rect class="headline-band" x="24" y="907" width="640" height="45" fill="var(--green)"/>
    <path class="outline-frame" d="M24,280 H495 Q540,280 556,322 L752,856 Q766,900 722,900 H24" fill="none" stroke="var(--white)" stroke-width="4"/>
    <path class="outline-frame" d="M1176,387 H1070 Q1040,387 1052,418 L1176,745" fill="none" stroke="var(--white)" stroke-width="4"/>
    <g class="slide-dots">
      <path d="M976,1065 H1004 Q1009,1065 1011,1070 L1014,1077 Q1015,1081 1011,1081 H974 Q969,1081 970,1077 Z" fill="var(--dark)"/>
      <path d="M1023,1065 H1051 Q1056,1065 1058,1070 L1061,1077 Q1062,1081 1058,1081 H1021 Q1016,1081 1017,1077 Z" fill="var(--green)"/>
      <path d="M1070,1065 H1098 Q1103,1065 1105,1070 L1108,1077 Q1109,1081 1105,1081 H1068 Q1063,1081 1064,1077 Z" fill="var(--dark)"/>
    </g>
  </svg>

  <div class="brand">
    <span class="brand-square"></span>
    <span class="brand-name">Dolvira</span>
  </div>

  <div class="contact">
    <span class="contact-label">More info</span>
    <span class="contact-phone">+0123 456 7890</span>
  </div>

  <h1 class="headline">
    <span class="headline-intro">We Are</span>
    <span class="headline-main">HIRING</span>
    <span class="headline-sub">Join Our<br>Team</span>
  </h1>

  <p class="tagline">IT system house Dolvira serves</p>

  <div class="cta">
    <span class="cta-label">JOIN US</span>
    <svg class="cta-arrow" width="18" height="23" viewBox="0 0 18 23">
      <path d="M4,3 L13,11.5 L4,20" fill="none" stroke="var(--green)" stroke-width="5" stroke-linecap="round" stroke-linejoin="round"/>
    </svg>
  </div>

  <p class="website">www.websitename.com</p>
</div>
</body>
</html>
```